Bright Harbour Painting

Hi
I'm looking for a unique and eye-catching design for my business card that reflects the identity of my business. We specialize in residential, commercial, insurance, real state, heritage,and body corporate painting services and I want the card to make a memorable impression on potential clients.

Key elements to include are:
- Our logo (attached)
- Contact information: my name is dariush kamrani but my short name is dar, im a director of this business, number: 0458307715, email: info@brightharbourpainting.com.au
Website: www.brightharbourpainting.com.au
Social media: facebook, instagram.

I'm open to creative ideas and unconventional formats, but it's important that the design maintains a professional look.

I'd like to see some initial concepts within the few days, and I'm willing to discuss any ideas you have.

Looking forward to seeing your creativity at work!

I prefer the colours pretty much the same as my logo, but i would be happy see if my logo match with other colours.
Thanks very much

Best regards,
Dar

Target Market(s)

Our target market consists of residential exterior and interior painting, basically we do all commercial jobs, bod corporate , heritage

Industry/Entity Type

Residential and commercial painting

Contact Information for Business Card

All my information as provided!! Im not sure if you guys have access to my logo through with all the format in my account??

Font styles to use
Serif

Requirements
Must have
• My business card should be double sided,
Nice to have
• Its nice to have all my information in front and the rest at the back, like what we we do like residential , interior exterior and as i mentioned

```html
<!DOCTYPE html>
<html lang="en">
<head>
<meta charset="utf-8">
<title>Bright Harbour Painting – Business Card</title>
<link rel="stylesheet" href="https://fonts.googleapis.com/css2?family=Arimo:wght@400;700&display=swap">
<style>
  :root {
    --stage: #d9dbde;
    --card-white: #ffffff;
    --brand-blue: #2f5fb3;
    --pattern-blue: #3567bd;
    --brand-green: #1f6b32;
    --brand-red: #c0282d;
    --ink-grey: #4a4a4a;
    --faint-tint: #eef1ee;
  }
  * { box-sizing: border-box; margin: 0; padding: 0; }
  html, body {
    width: 1200px; height: 900px; overflow: hidden;
    background: var(--stage);
    font-family: "Arimo", Arial, sans-serif;
  }
  .canvas {
    width: 1200px; height: 900px;
    display: flex; flex-direction: column; align-items: center; justify-content: center;
    gap: 36px;
  }
  .card {
    position: relative; width: 720px; height: 412px; overflow: hidden;
    box-shadow: 0 6px 18px rgba(0,0,0,.18);
  }

  /* Back side */
  .card-back { background: var(--brand-blue); }
  .card-back .pattern-field {
    position: absolute; inset: 0;
    background: linear-gradient(135deg, var(--pattern-blue), var(--brand-blue) 60%, #2b57a6);
  }
  .card-back .back-centre {
    position: absolute; left: 0; right: 0; top: 140px;
    text-align: center; color: var(--card-white);
  }
  .back-brand {
    display: inline-flex; align-items: center; gap: 10px;
    font-size: 20px; font-weight: 700; letter-spacing: .5px; margin-bottom: 34px;
  }
  .back-brand .brand-square { width: 16px; height: 16px; background: var(--card-white); }
  .services { font-size: 17px; line-height: 1.45; }

  /* Front side */
  .card-front { background: var(--card-white); }
  .name-tab {
    position: absolute; right: 0; top: 40px; width: 24px; height: 38px;
    background: var(--brand-green);
  }
  .holder {
    position: absolute; right: 44px; top: 36px; text-align: right;
  }
  .holder-name { font-size: 30px; font-weight: 700; letter-spacing: .5px; text-transform: uppercase; }
  .holder-name .first { color: var(--brand-green); }
  .holder-name .last { color: var(--brand-blue); }
  .holder-role { font-size: 16px; color: var(--ink-grey); margin-top: 2px; }

  .faint-mark {
    position: absolute; right: 40px; top: 150px; width: 190px; height: 190px;
    background: var(--faint-tint);
  }

  .front-brand {
    position: absolute; left: 56px; top: 140px;
    display: flex; align-items: center; gap: 14px;
  }
  .front-brand .brand-square { width: 26px; height: 26px; background: var(--brand-green); }
  .front-brand .brand-name {
    font-size: 30px; font-weight: 700; color: var(--brand-green); letter-spacing: .5px;
  }

  .contacts {
    position: absolute; left: 56px; bottom: 40px;
    list-style: none; font-size: 19px; color: var(--ink-grey); line-height: 1.5;
  }
  .contacts li { display: flex; align-items: center; gap: 10px; }
  .contacts svg { width: 16px; height: 16px; fill: var(--brand-blue); flex: none; }
  .social-dots { display: inline-flex; gap: 4px; }
  .social-dots span { width: 14px; height: 14px; border-radius: 50%; background: var(--brand-blue); }
</style>
</head>
<body>
<main class="canvas">

  <section class="card card-back" aria-label="Card back">
    <div class="pattern-field" role="img" aria-label="Repeating embossed brand pattern in blue tones"></div>
    <div class="back-centre">
      <div class="back-brand"><span class="brand-square"></span>Bright Harbour Painting</div>
      <p class="services">Residential I Commercial I Insurance I Real State I Heritage<br>Body Corporate Painting</p>
    </div>
  </section>

  <section class="card card-front" aria-label="Card front">
    <div class="name-tab"></div>
    <div class="holder">
      <p class="holder-name"><span class="first">Dariush</span> <span class="last">Kamrani</span></p>
      <p class="holder-role">Director</p>
    </div>
    <div class="faint-mark" aria-hidden="true"></div>

    <div class="front-brand">
      <span class="brand-square"></span>
      <span class="brand-name">Bright Harbour Painting</span>
    </div>

    <ul class="contacts">
      <li>
        <svg viewBox="0 0 16 16" aria-hidden="true"><path d="M3 2h3l1 4-2 1c1 2 2 3 4 4l1-2 4 1v3c0 1-1 2-2 2C6 15 1 10 1 4c0-1 1-2 2-2z"/></svg>
        0458307715
      </li>
      <li>
        <svg viewBox="0 0 16 16" aria-hidden="true"><path d="M1 3h14v10H1z M2 4l6 5 6-5" fill="none" stroke="#2f5fb3" stroke-width="1.6"/></svg>
        info@brightharbourpainting.com.au
      </li>
      <li>
        <svg viewBox="0 0 16 16" aria-hidden="true"><circle cx="8" cy="8" r="6.5" fill="none" stroke="#2f5fb3" stroke-width="1.5"/><path d="M1.5 8h13M8 1.5c-3 3-3 10 0 13M8 1.5c3 3 3 10 0 13" fill="none" stroke="#2f5fb3" stroke-width="1.2"/></svg>
        www.brightharbourpainting.com.au
      </li>
      <li>
        <span class="social-dots" aria-hidden="true"><span></span><span></span></span>
        brightharbourpainting
      </li>
    </ul>
  </section>

</main>
</body>
</html>
```